Webdesign für Honigmanufaktur
Zielgruppe
Imkerei, Verkauf von Honig und Honigerzeugnissen, so wie Bienenwachskerzen.
Zielgruppe sind vermutlich Frauen im mittleren bis gehobenen Alter.
Aufgabenstellung
Es gibt ein Firmenlogo.
Ich bevorzuge als Grundfarbe weiß, lasse mich aber von guten Einfällen gerne überraschen.
Die Website www.velunda.at finde ich sehr ansprechend.
Nur ohne Musik.
Ohne Deutsch/Englisch Auswahl.
Es soll danach Word press verwendet werden.

```html
<!DOCTYPE html>
<html lang="de">
<head>
<meta charset="utf-8">
<title>Honigmanufaktur Lindenhain – Webdesign</title>
<link href="https://fonts.googleapis.com/css2?family=Roboto:wght@400;700&family=Roboto+Condensed:wght@400;700&display=swap" rel="stylesheet">
<style>
:root{
  --bg:#f0f0f0;
  --white:#ffffff;
  --honey:#f0a430;
  --brown:#5a3817;
  --text:#4a4a4a;
  --muted:#8a8a8a;
  --line:#e6e6e6;
}
*{margin:0;padding:0;box-sizing:border-box}
html,body{width:1200px;height:3720px;overflow:hidden;background:var(--bg)}
body{position:relative;font-family:"Roboto",sans-serif;color:var(--text)}
.page{position:absolute;left:56px;width:1088px;height:858px;background:var(--white);box-shadow:0 2px 10px rgba(0,0,0,.08)}
.page--1{top:56px}.page--2{top:970px}.page--3{top:1884px}.page--4{top:2798px}

.account{position:absolute;top:7px;left:753px;width:118px;display:flex;justify-content:space-between;padding-bottom:5px;border-bottom:1px solid var(--line);font-family:"Roboto Condensed",sans-serif;font-size:6.5px;letter-spacing:1.2px;color:var(--muted)}
.header-line{position:absolute;top:91px;left:0;width:100%;height:1px;background:var(--line)}
.brand{position:absolute;top:6px;left:444px;width:200px;text-align:center;font-family:"Roboto Condensed",sans-serif;font-weight:700;color:var(--brown)}
.brand__dot{display:block;width:30px;height:30px;margin:0 auto 4px;border-radius:50%;background:var(--honey)}
.brand__name{display:block;font-size:12px;letter-spacing:.5px;line-height:13px}
.brand__place{display:block;font-size:8px;letter-spacing:3px;line-height:10px}
.nav__item{position:absolute;top:66px;transform:translateX(-50%);font-family:"Roboto Condensed",sans-serif;font-size:7.5px;letter-spacing:1.6px;color:var(--muted);white-space:nowrap}
.nav__item--active{color:var(--honey)}

.photo{position:absolute;top:114px;height:205px}
.photo--wide{left:208px;width:380px}
.photo--left{left:208px;width:328px}
.photo--right{left:542px;width:329px}
.cutout{position:absolute}
.cutout--large{left:634px;top:204px;width:234px;height:231px}
.cutout--small{left:658px;top:360px;width:152px;height:110px}

.intro__title{position:absolute;top:342px;left:208px;font-family:"Roboto Condensed",sans-serif;font-size:11px;letter-spacing:1.6px;color:var(--honey);font-weight:400}
.intro__text{position:absolute;top:362px;left:208px;width:382px;font-size:8.3px;line-height:13.6px;letter-spacing:.35px}

.footer-rule{position:absolute;top:527px;left:200px;width:678px;height:2px;background:var(--honey)}
.footer-col{position:absolute;top:552px;width:150px;font-size:7.2px;line-height:13.8px;color:var(--muted)}
.footer-col h4{font-size:8.2px;font-weight:700;color:#333;margin-bottom:13px}
.footer-col strong{color:#333}
.footer-col--1{left:208px}.footer-col--2{left:379px}.footer-col--3{left:548px}.footer-col--4{left:717px}
.social{position:absolute;top:701px;left:208px;display:flex;gap:11px}
.social span{width:7px;height:7px;border-radius:50%;background:#555}
.footer-divider{position:absolute;top:741px;left:0;width:100%;height:1px;background:var(--line)}
.copyright{position:absolute;top:765px;left:0;width:100%;text-align:center;font-size:6.5px;color:var(--muted)}
.payments{position:absolute;top:786px;left:453px;display:flex;gap:9px}
.payments span{width:29px;height:17px;border:1px solid var(--line);border-radius:2px;background:#fafafa}
</style>
</head>
<body>

<!-- Seite 1: Startseite -->
<section class="page page--1">
  <div class="account"><span>MEIN KONTO</span><span>WARENKORB (0)</span></div>
  <div class="brand"><span class="brand__dot"></span><span class="brand__name">HONIGMANUFAKTUR</span><span class="brand__place">LINDENHAIN</span></div>
  <nav>
    <span class="nav__item nav__item--active" style="left:257px">STARTSEITE</span>
    <span class="nav__item" style="left:348px">DIE MANUFAKTUR</span>
    <span class="nav__item" style="left:438px">DER HONIG</span>
    <span class="nav__item" style="left:656px">DAS BIENENWACHS</span>
    <span class="nav__item" style="left:754px">DER SHOP</span>
    <span class="nav__item" style="left:835px">KONTAKT</span>
  </nav>
  <div class="header-line"></div>
  <div class="photo photo--wide" role="img" aria-label="Lavendelblüten mit Biene auf grüner Wiese" style="background:linear-gradient(180deg,#6f7a5a 0%,#8a7fb8 35%,#6d8a4a 70%,#4f6b32 100%)"></div>
  <div class="cutout cutout--large" role="img" aria-label="Honiglöffel aus Holz, von dem Honig tropft" style="background:radial-gradient(ellipse at 50% 55%,#f0a020 0%,#f5c050 35%,rgba(255,255,255,0) 70%)"></div>
  <h2 class="intro__title">DIE HONIGMANUFAKTUR LINDENHAIN</h2>
  <p class="intro__text">Die Honigmanufaktur Lindenhain ist eine kleine, feine Bio-Honig-Manufaktur mit dem großen Ehrgeiz, Ihnen den feinsten und besten Honig zu liefern, den Sie je gekostet haben. Lorem ipsum dolor sit amet, consetetur sadipscing elitr, sed diam nonumy eirmod tempor invidunt ut labore et dolore magna aliquyam erat, sed diam voluptua. At vero eos et accusam et justo duo dolores et ea rebum. Stet clita kasd gubergren, no sea takimata sanctus est Lorem ipsum dolor sit amet. Lorem ipsum dolor sit amet, consetetur sadipscing elitr, sed diam nonumy eirmod tempor invidunt ut labore et dolore magna aliquyam erat, sed diam voluptua.</p>
  <div class="footer-rule"></div>
  <div class="footer-col footer-col--1"><h4>Honigmanufaktur © 2018</h4>Lorem ipsum dolor sit amet, consetetur sadipscing elitr, sed diam nonumy eirmod tempor invidunt ut labore et dolore magna aliquyam erat, sed diam voluptua. Lorem ipsum dolor sit amet, consetetur sadipscing<br><br><strong>Telefon:</strong> 0000 000 0000<br><strong>E-Mail:</strong> service@lindenhain-honig.de</div>
  <div class="footer-col footer-col--2"><h4>Unternehmen</h4>Die Manufaktur<br>Der Honig<br>Das Bienenwachs<br>Kontaktformular<br>Datenschutz<br>Impressum</div>
  <div class="footer-col footer-col--3"><h4>Service</h4>FAQ<br>Lieferung &amp; Versand<br>AGB<br>Widerrufsbelehrung<br>Widerrufsformular<br>Glossar<br>Kundenmeinungen</div>
  <div class="footer-col footer-col--4"><h4>Mein Konto</h4>Kundenkonto anlegen<br>Meine Bestellungen<br>Meine Nachrichten<br>Mein Wunschzettel<br>Produkte vergleichen</div>
  <div class="social"><span></span><span></span><span></span><span></span><span></span></div>
  <div class="footer-divider"></div>
  <p class="copyright">Copyright © 2018 Honigmanufaktur | Musterstraße 10 | 12345 Musterstadt | Tel. 012 345 678 | Fax 012 345 678 | info@lindenhain-honig.de</p>
  <div class="payments"><span></span><span></span><span></span><span></span><span></span></div>
</section>

<!-- Seite 2: Die Manufaktur -->
<section class="page page--2">
  <div class="account"><span>MEIN KONTO</span><span>WARENKORB (0)</span></div>
  <div class="brand"><span class="brand__dot"></span><span class="brand__name">HONIGMANUFAKTUR</span><span class="brand__place">LINDENHAIN</span></div>
  <nav>
    <span class="nav__item" style="left:257px">STARTSEITE</span>
    <span class="nav__item nav__item--active" style="left:348px">DIE MANUFAKTUR</span>
    <span class="nav__item" style="left:438px">DER HONIG</span>
    <span class="nav__item" style="left:656px">DAS BIENENWACHS</span>
    <span class="nav__item" style="left:754px">DER SHOP</span>
    <span class="nav__item" style="left:835px">KONTAKT</span>
  </nav>
  <div class="header-line"></div>
  <div class="photo photo--left" role="img" aria-label="Bienen am Einflugloch eines Bienenstocks" style="background:linear-gradient(135deg,#e8e8e6 0%,#b8b4ac 45%,#a4783e 80%,#6b4a22 100%)"></div>
  <div class="photo photo--right" role="img" aria-label="Imker in Schutzanzug mit einer Wabe im Garten" style="background:linear-gradient(135deg,#c9d3b2 0%,#eeeeea 40%,#e2e2dc 65%,#8aa05a 100%)"></div>
  <div class="cutout cutout--small" role="img" aria-label="Freigestellte Biene im Flug" style="background:radial-gradient(ellipse at 50% 50%,#6a5a3a 0%,#c7b48a 28%,rgba(255,255,255,0) 62%)"></div>
  <h2 class="intro__title">DAS PRODUKTIONSTEAM DER HONIGMANUFAKTUR</h2>
  <p class="intro__text">Lorem ipsum dolor sit amet, consetetur sadipscing elitr, sed diam nonumy eirmod tempor invidunt ut labore et dolore magna aliquyam erat, sed diam voluptua. At vero eos et accusam et justo duo dolores et ea rebum. Stet clita kasd gubergren, no sea takimata sanctus est Lorem ipsum dolor sit amet. Lorem ipsum dolor sit amet, consetetur sadipscing elitr, sed diam nonumy eirmod tempor invidunt ut labore et dolore magna aliquyam erat, sed diam voluptua. At vero eos et accusam et justo duo dolores et ea rebum. Stet clita kasd gubergren, no sea takimata sanctus est Lorem ipsum dolor sit amet lorem ipsum dolor sit amet.</p>
  <div class="footer-rule"></div>
  <div class="footer-col footer-col--1"><h4>Honigmanufaktur © 2018</h4>Lorem ipsum dolor sit amet, consetetur sadipscing elitr, sed diam nonumy eirmod tempor invidunt ut labore et dolore magna aliquyam erat, sed diam voluptua. Lorem ipsum dolor sit amet, consetetur sadipscing<br><br><strong>Telefon:</strong> 0000 000 0000<br><strong>E-Mail:</strong> service@lindenhain-honig.de</div>
  <div class="footer-col footer-col--2"><h4>Unternehmen</h4>Die Manufaktur<br>Der Honig<br>Das Bienenwachs<br>Kontaktformular<br>Datenschutz<br>Impressum</div>
  <div class="footer-col footer-col--3"><h4>Service</h4>FAQ<br>Lieferung &amp; Versand<br>AGB<br>Widerrufsbelehrung<br>Widerrufsformular<br>Glossar<br>Kundenmeinungen</div>
  <div class="footer-col footer-col--4"><h4>Mein Konto</h4>Kundenkonto anlegen<br>Meine Bestellungen<br>Meine Nachrichten<br>Mein Wunschzettel<br>Produkte vergleichen</div>
  <div class="social"><span></span><span></span><span></span><span></span><span></span></div>
  <div class="footer-divider"></div>
  <p class="copyright">Copyright © 2018 Honigmanufaktur | Musterstraße 10 | 12345 Musterstadt | Tel. 012 345 678 | Fax 012 345 678 | info@lindenhain-honig.de</p>
  <div class="payments"><span></span><span></span><span></span><span></span><span></span></div>
</section>

<!-- Seite 3: Der Honig -->
<section class="page page--3">
  <div class="account"><span>MEIN KONTO</span><span>WARENKORB (0)</span></div>
  <div class="brand"><span class="brand__dot"></span><span class="brand__name">HONIGMANUFAKTUR</span><span class="brand__place">LINDENHAIN</span></div>
  <nav>
    <span class="nav__item" style="left:257px">STARTSEITE</span>
    <span class="nav__item" style="left:348px">DIE MANUFAKTUR</span>
    <span class="nav__item nav__item--active" style="left:438px">DER HONIG</span>
    <span class="nav__item" style="left:656px">DAS BIENENWACHS</span>
    <span class="nav__item" style="left:754px">DER SHOP</span>
    <span class="nav__item" style="left:835px">KONTAKT</span>
  </nav>
  <div class="header-line"></div>
  <div class="photo photo--left" role="img" aria-label="Honigglas mit Heidekraut und Honiglöffel auf Holztisch" style="background:linear-gradient(135deg,#ecebe8 0%,#a3739a 35%,#e9a33a 65%,#d8d4cc 100%)"></div>
  <div class="photo photo--right" role="img" aria-label="Hände, die Honig in eine Schale geben" style="background:linear-gradient(135deg,#a8c6d4 0%,#f2f0ec 45%,#efe6d6 70%,#cfdde2 100%)"></div>
  <div class="cutout cutout--small" role="img" aria-label="Freigestellte Honigwabe" style="background:radial-gradient(ellipse at 50% 50%,#f0a820 0%,#f7c860 32%,rgba(255,255,255,0) 64%)"></div>
  <h2 class="intro__title">DIE GESUNDHEITLICHEN VORTEILE VON HONIG</h2>
  <p class="intro__text">Lorem ipsum dolor sit amet, consetetur sadipscing elitr, sed diam nonumy eirmod tempor invidunt ut labore et dolore magna aliquyam erat, sed diam voluptua. At vero eos et accusam et justo duo dolores et ea rebum. Stet clita kasd gubergren, no sea takimata sanctus est Lorem ipsum dolor sit amet. Lorem ipsum dolor sit amet, consetetur sadipscing elitr, sed diam nonumy eirmod tempor invidunt ut labore et dolore magna aliquyam erat, sed diam voluptua. At vero eos et accusam et justo duo dolores et ea rebum. Stet clita kasd gubergren, no sea takimata sanctus est Lorem ipsum dolor sit amet lorem ipsum dolor sit amet.</p>
  <div class="footer-rule"></div>
  <div class="footer-col footer-col--1"><h4>Honigmanufaktur © 2018</h4>Lorem ipsum dolor sit amet, consetetur sadipscing elitr, sed diam nonumy eirmod tempor invidunt ut labore et dolore magna aliquyam erat, sed diam voluptua. Lorem ipsum dolor sit amet, consetetur sadipscing<br><br><strong>Telefon:</strong> 0000 000 0000<br><strong>E-Mail:</strong> service@lindenhain-honig.de</div>
  <div class="footer-col footer-col--2"><h4>Unternehmen</h4>Die Manufaktur<br>Der Honig<br>Das Bienenwachs<br>Kontaktformular<br>Datenschutz<br>Impressum</div>
  <div class="footer-col footer-col--3"><h4>Service</h4>FAQ<br>Lieferung &amp; Versand<br>AGB<br>Widerrufsbelehrung<br>Widerrufsformular<br>Glossar<br>Kundenmeinungen</div>
  <div class="footer-col footer-col--4"><h4>Mein Konto</h4>Kundenkonto anlegen<br>Meine Bestellungen<br>Meine Nachrichten<br>Mein Wunschzettel<br>Produkte vergleichen</div>
  <div class="social"><span></span><span></span><span></span><span></span><span></span></div>
  <div class="footer-divider"></div>
  <p class="copyright">Copyright © 2018 Honigmanufaktur | Musterstraße 10 | 12345 Musterstadt | Tel. 012 345 678 | Fax 012 345 678 | info@lindenhain-honig.de</p>
  <div class="payments"><span></span><span></span><span></span><span></span><span></span></div>
</section>

<!-- Seite 4: Das Bienenwachs -->
<section class="page page--4">
  <div class="account"><span>MEIN KONTO</span><span>WARENKORB (0)</span></div>
  <div class="brand"><span class="brand__dot"></span><span class="brand__name">HONIGMANUFAKTUR</span><span class="brand__place">LINDENHAIN</span></div>
  <nav>
    <span class="nav__item" style="left:257px">STARTSEITE</span>
    <span class="nav__item" style="left:348px">DIE MANUFAKTUR</span>
    <span class="nav__item" style="left:438px">DER HONIG</span>
    <span class="nav__item nav__item--active" style="left:656px">DAS BIENENWACHS</span>
    <span class="nav__item" style="left:754px">DER SHOP</span>
    <span class="nav__item" style="left:835px">KONTAKT</span>
  </nav>
  <div class="header-line"></div>
  <div class="photo photo--left" role="img" aria-label="Bienen auf goldenen Honigwaben" style="background:linear-gradient(135deg,#d99a1e 0%,#f0bd3e 40%,#c88418 75%,#e4ac30 100%)"></div>
  <div class="photo photo--right" role="img" aria-label="Bienenwachskerzen und Honiggläser auf Holz" style="background:linear-gradient(180deg,#8a5a2a 0%,#c8904a 40%,#e8c890 70%,#c08850 100%)"></div>
  <div class="cutout cutout--small" role="img" aria-label="Freigestellte Honiggläser mit Wabe und Blüten" style="background:radial-gradient(ellipse at 50% 50%,#e08a20 0%,#f4c060 32%,rgba(255,255,255,0) 64%)"></div>
  <h2 class="intro__title">DAS ALLES KANN BIENENWACHS</h2>
  <p class="intro__text">Lorem ipsum dolor sit amet, consetetur sadipscing elitr, sed diam nonumy eirmod tempor invidunt ut labore et dolore magna aliquyam erat, sed diam voluptua. At vero eos et accusam et justo duo dolores et ea rebum. Stet clita kasd gubergren, no sea takimata sanctus est Lorem ipsum dolor sit amet. Lorem ipsum dolor sit amet, consetetur sadipscing elitr, sed diam nonumy eirmod tempor invidunt ut labore et dolore magna aliquyam erat, sed diam voluptua. At vero eos et accusam et justo duo dolores et ea rebum. Stet clita kasd gubergren, no sea takimata sanctus est Lorem ipsum dolor sit amet lorem ipsum dolor sit amet.</p>
  <div class="footer-rule"></div>
  <div class="footer-col footer-col--1"><h4>Honigmanufaktur © 2018</h4>Lorem ipsum dolor sit amet, consetetur sadipscing elitr, sed diam nonumy eirmod tempor invidunt ut labore et dolore magna aliquyam erat, sed diam voluptua. Lorem ipsum dolor sit amet, consetetur sadipscing<br><br><strong>Telefon:</strong> 0000 000 0000<br><strong>E-Mail:</strong> service@lindenhain-honig.de</div>
  <div class="footer-col footer-col--2"><h4>Unternehmen</h4>Die Manufaktur<br>Der Honig<br>Das Bienenwachs<br>Kontaktformular<br>Datenschutz<br>Impressum</div>
  <div class="footer-col footer-col--3"><h4>Service</h4>FAQ<br>Lieferung &amp; Versand<br>AGB<br>Widerrufsbelehrung<br>Widerrufsformular<br>Glossar<br>Kundenmeinungen</div>
  <div class="footer-col footer-col--4"><h4>Mein Konto</h4>Kundenkonto anlegen<br>Meine Bestellungen<br>Meine Nachrichten<br>Mein Wunschzettel<br>Produkte vergleichen</div>
  <div class="social"><span></span><span></span><span></span><span></span><span></span></div>
  <div class="footer-divider"></div>
  <p class="copyright">Copyright © 2018 Honigmanufaktur | Musterstraße 10 | 12345 Musterstadt | Tel. 012 345 678 | Fax 012 345 678 | info@lindenhain-honig.de</p>
  <div class="payments"><span></span><span></span><span></span><span></span><span></span></div>
</section>

</body>
</html>
```